HWN Structures Ltd- building and maintenance company looking to create professional branding for m

creation of a website for a building and maintenance company,
will need a gallery and references/ reviews page
homepage to have some company information with rolling photos of completed works
all suggestions welcome on additional requirements for website.
layout should be easy to navigate.

Target Market(s)

30-70s homeowners with mid to high income

Logo Text

HWN Structures Ltd

Coding

Coded - Design and coding required

Number of Pages Required

4 page

```html
<!DOCTYPE html>
<html lang="en">
<head>
<meta charset="utf-8">
<title>HWN Structures Ltd – Home</title>
<link href="https://fonts.googleapis.com/css2?family=Roboto:wght@300;400;500;700&family=Lato:wght@400;700&family=Prata&display=swap" rel="stylesheet">
<style>
:root{
  --navy:#0c2560;
  --navy-deep:#081b48;
  --orange:#f25a1c;
  --ink:#1c2a4a;
  --muted:#7a8090;
  --line:#e4e6ec;
  --white:#ffffff;
}
*{margin:0;padding:0;box-sizing:border-box}
html,body{width:1200px;height:4976px;overflow:hidden;background:#fff}
body{font-family:"Lato",sans-serif;color:var(--ink);position:relative}
.page{position:absolute;left:127px;top:82px;width:940px;background:#fff;box-shadow:0 0 22px rgba(0,0,0,.12)}
section,header,footer{position:relative;width:940px}
.abs{position:absolute}
.eyebrow{font-size:9px;letter-spacing:.5px;text-transform:uppercase;color:var(--muted);text-align:center;width:100%}
.sec-title{font-family:"Roboto",sans-serif;font-weight:700;font-size:28px;color:var(--navy);text-align:center;width:100%}
.btn{background:var(--orange);color:#fff;font-size:9px;text-transform:uppercase;display:flex;align-items:center;justify-content:center;font-family:"Roboto",sans-serif}
.photo{position:absolute}

/* header */
.site-header{height:86px}
.brand{left:19px;top:29px;display:flex;align-items:center;gap:6px}
.brand-mark{width:26px;height:26px;background:var(--orange)}
.brand-name{font-family:"Roboto",sans-serif;font-weight:700;font-size:15px;color:var(--navy)}
.hiring{left:277px;top:14px;font-size:9px;color:var(--muted)}
.hiring b{color:var(--navy)}
.nav{top:52px;font-size:9px;color:var(--ink)}
.ask{left:765px;top:30px;font-size:9px;color:var(--muted)}
.ask-phone{left:775px;top:45px;font-size:9px;color:var(--orange);font-weight:700}
.search{left:905px;top:36px}

/* hero */
.hero{height:491px;background:linear-gradient(110deg,#3a2f25 0%,#6b5840 40%,#a58760 65%,#5b4a36 100%)}
.hero-title{left:84px;top:126px;font-family:"Prata",serif;font-size:72px;font-weight:400;color:#fff;letter-spacing:1px}
.hero-sub{left:84px;top:236px;width:430px;font-size:15px;line-height:31px;color:#fff}
.hero-btn{left:84px;top:312px;width:109px;height:30px}
.stats{left:84px;top:454px;width:780px;height:75px;background:#fff;box-shadow:0 2px 10px rgba(0,0,0,.08);display:flex;z-index:2}
.stat{flex:1;text-align:center;padding-top:20px;border-right:1px solid var(--line)}
.stat:last-child{border-right:none}
.stat-num{font-family:"Roboto",sans-serif;font-weight:500;font-size:14px;color:var(--navy)}
.stat-label{font-size:8px;color:var(--orange);text-transform:uppercase;margin-top:5px}

/* about */
.about{height:474px}
.about-title{left:84px;top:100px;font-family:"Roboto",sans-serif;font-weight:700;font-size:22px;line-height:30px;color:var(--navy)}
.about-text{left:339px;top:76px;width:508px;font-size:10px;line-height:19px;color:#444}

/* services */
.services{height:433px}
.service{width:250px;display:flex;gap:10px}
.service svg{flex:none}
.service h3{font-family:"Roboto",sans-serif;font-size:12px;font-weight:500;color:var(--navy);margin-bottom:6px}
.service p{font-size:10px;line-height:19px;color:#555;width:205px}

/* process */
.process{height:401px;background:var(--navy);color:#fff}
.process .eyebrow{color:#cfd6ea}
.process .sec-title{color:#fff}
.step{width:230px}
.step-num{font-family:"Roboto",sans-serif;font-weight:300;font-size:84px;line-height:1}
.step h3{font-family:"Roboto",sans-serif;font-weight:400;font-size:14px;margin-top:28px}
.step p{font-size:9.5px;line-height:19px;margin-top:12px;color:#e4e8f4}
.divider{width:1px;height:188px;background:rgba(255,255,255,.25);top:148px}

/* projects */
.projects{height:829px}
.project{width:246px;text-align:center}
.project h3{font-family:"Roboto",sans-serif;font-weight:400;font-size:14px;color:var(--ink);margin-top:26px}
.project p{font-size:10px;line-height:19px;color:var(--muted);margin-top:12px;padding:0 4px}
.project a{display:block;font-size:10px;color:var(--orange);text-decoration:none;margin-top:12px}
.project .photo{position:static;height:150px}

/* mission */
.mission{height:321px}
.mission-panel{left:0;top:0;width:474px;height:321px;background:var(--navy)}
.mission-title{left:84px;top:44px;font-family:"Roboto",sans-serif;font-weight:700;font-size:38px;color:#fff}
.mission-text{left:84px;top:99px;width:380px;font-size:9.5px;line-height:19px;color:#fff}
.mission-btn{left:84px;top:246px;width:109px;height:30px}

/* team */
.team{height:623px}
.member{width:240px;text-align:center}
.avatar{width:188px;height:188px;border-radius:50%;margin:0 auto;position:relative;background:linear-gradient(160deg,#dfe4ec,#3b5b8d 60%,#e08a2e)}
.avatar .plus{position:absolute;right:8px;top:112px;width:30px;height:30px;border-radius:50%;background:var(--orange);color:#fff;font-size:20px;line-height:26px;text-align:center;border:2px solid #fff}
.member h3{font-family:"Roboto",sans-serif;font-weight:400;font-size:18px;color:var(--navy);margin-top:22px}
.member span{font-size:10px;color:var(--muted)}

/* management */
.management{height:364px;background:linear-gradient(90deg,#d5d9df 0%,#c0c7d2 30%,#6f7380 60%,#5a5d66 100%)}
.mgmt-box{left:504px;top:41px;width:360px;height:279px;background:var(--orange);color:#fff;padding:44px 46px}
.mgmt-box h2{font-family:"Roboto",sans-serif;font-weight:400;font-size:34px;line-height:36px}
.mgmt-box p{font-size:10px;line-height:19px;margin-top:16px;width:270px}
.mgmt-btn{margin-top:16px;width:116px;height:32px;border:1px solid #fff;font-size:9px;text-transform:uppercase;display:flex;align-items:center;justify-content:center;font-family:"Roboto",sans-serif}

/* testimonials */
.testimonials{height:362px;background:linear-gradient(180deg,#f1f2f4,#e7e8eb)}
.quote{left:180px;top:176px;width:580px;text-align:center;font-size:10px;line-height:19px;color:#666}
.client{top:222px;width:100%;text-align:center;font-family:"Roboto",sans-serif;font-size:11px;color:var(--ink);text-transform:uppercase}
.client-role{top:240px;width:100%;text-align:center;font-size:8px;color:var(--muted);text-transform:uppercase}
.dots{top:258px;width:100%;display:flex;justify-content:center;gap:6px}
.dots i{width:5px;height:5px;border-radius:50%;background:#999}
.dots i:first-child{background:var(--navy)}

/* footer */
.site-footer{height:285px;background:var(--navy);color:#fff}
.f-col h4{font-family:"Roboto",sans-serif;font-weight:400;font-size:12px;margin-bottom:20px}
.f-col p{font-size:9.5px;line-height:26px}
.socials{display:flex;gap:14px;margin-top:12px}
.socials i{width:24px;height:24px;border:1px solid rgba(255,255,255,.7);border-radius:50%}
.thumbs{display:grid;grid-template-columns:repeat(3,60px);grid-template-rows:repeat(2,58px);gap:5px;margin-top:-4px}
.thumbs div{background:linear-gradient(135deg,#c89a64,#7a5434)}
.thumbs div:nth-child(even){background:linear-gradient(135deg,#d8c4a5,#8b6b4a)}
.f-bottom{left:0;top:242px;width:940px;height:43px;background:var(--navy-deep);font-size:8px;display:flex;align-items:center;justify-content:center}
</style>
</head>
<body>
<div class="page">

  <header class="site-header">
    <div class="abs brand"><span class="brand-mark"></span><span class="brand-name">HWN Structures Ltd</span></div>
    <div class="abs hiring"><b>Now Hiring:</b> Are you a driven and motivated 1st Line IT Support Engineer?</div>
    <span class="abs nav" style="left:286px">Home</span>
    <span class="abs nav" style="left:340px">Company</span>
    <span class="abs nav" style="left:409px">Company</span>
    <span class="abs nav" style="left:478px">Contact Us</span>
    <span class="abs nav" style="left:553px">About Us</span>
    <span class="abs nav" style="left:622px">Blogs</span>
    <div class="abs ask">Have any questions?</div>
    <div class="abs ask-phone">+44 1632 960 418</div>
    <svg class="abs search" width="12" height="12" viewBox="0 0 12 12"><circle cx="5" cy="5" r="3.6" fill="none" stroke="#1c2a4a" stroke-width="1.5"/><line x1="7.6" y1="7.6" x2="11" y2="11" stroke="#1c2a4a" stroke-width="1.5"/></svg>
  </header>

  <section class="hero" role="img" aria-label="Builder measuring and marking timber on a construction site">
    <h1 class="abs hero-title">Construction</h1>
    <p class="abs hero-sub">We set the standards others try to live up to. With more than 20 years of experience</p>
    <div class="abs btn hero-btn">Learn More</div>
    <div class="abs stats">
      <div class="stat"><div class="stat-num">156+</div><div class="stat-label">Projects Design</div></div>
      <div class="stat"><div class="stat-num">413+</div><div class="stat-label">Happy Customers</div></div>
      <div class="stat"><div class="stat-num">90</div><div class="stat-label">Ongoing Project</div></div>
      <div class="stat"><div class="stat-num">247</div><div class="stat-label">Construction Site</div></div>
    </div>
  </section>

  <section class="about">
    <h2 class="abs about-title">Builder Company,<br>Serving Since 1975.</h2>
    <p class="abs about-text">Lorem ipsum, or lipsum as it is sometimes known, is dummy text used in laying out print, graphic or web designs. The passage is attributed to an unknown typesetter in the 15th century who is thought to have scrambled parts of an old Latin treatise on duty and ethics for use in a type specimen book. Easily generate Lorem Ipsum placeholder text in any number of characters, words sentences or paragraphs. earn about the origins of the passage</p>
    <div class="photo" role="img" aria-label="Builders in hard hats measuring a plank with a tape measure" style="left:56px;top:191px;width:838px;height:281px;background:linear-gradient(100deg,#d9c9a8 0%,#b8935e 35%,#e3c46a 60%,#8c7456 100%)"></div>
  </section>

  <section class="services">
    <div class="abs eyebrow" style="top:60px;text-transform:none">What we do?</div>
    <h2 class="abs sec-title" style="top:80px">Our Services</h2>
    <div class="abs service" style="left:92px;top:159px">
      <svg width="30" height="30" viewBox="0 0 30 30" fill="none" stroke="#f25a1c" stroke-width="1.3"><circle cx="11" cy="9" r="5"/><path d="M3 26c0-6 4-9 8-9s8 3 8 9"/><rect x="19" y="16" width="8" height="8"/></svg>
      <div><h3>Lighting Protection</h3><p>Lorem ipsum dolor sit amet, consectetur adipiscing elit. Ut elit tellus, luctus nec ullamcorper mattis, pulvinar dapibus leo.</p></div>
    </div>
    <div class="abs service" style="left:352px;top:159px">
      <svg width="30" height="30" viewBox="0 0 30 30" fill="none" stroke="#f25a1c" stroke-width="1.3"><path d="M15 3 L5 12 V27 H25 V12 Z"/><path d="M15 13c-3 4-4 6-4 8a4 4 0 0 0 8 0c0-2-1-4-4-8z"/></svg>
      <div><h3>Water Supply</h3><p>Lorem ipsum dolor sit amet, consectetur adipiscing elit. Ut elit tellus, luctus nec ullamcorper mattis, pulvinar dapibus leo.</p></div>
    </div>
    <div class="abs service" style="left:613px;top:159px">
      <svg width="30" height="30" viewBox="0 0 30 30" fill="none" stroke="#f25a1c" stroke-width="1.3"><rect x="4" y="3" width="22" height="24"/><path d="M9 9h12M9 14h12M9 19h8"/></svg>
      <div><h3>Energy Distribution</h3><p>Lorem ipsum dolor sit amet, consectetur adipiscing elit. Ut elit tellus, luctus nec ullamcorper mattis, pulvinar dapibus leo.</p></div>
    </div>
    <div class="abs service" style="left:92px;top:279px">
      <svg width="30" height="30" viewBox="0 0 30 30" fill="none" stroke="#f25a1c" stroke-width="1.3"><rect x="3" y="5" width="24" height="16"/><path d="M10 26h10M15 21v5M8 10h14M8 15h9"/></svg>
      <div><h3>Building Control System</h3><p>Lorem ipsum dolor sit amet, consectetur adipiscing elit. Ut elit tellus, luctus nec ullamcorper mattis, pulvinar dapibus leo.</p></div>
    </div>
    <div class="abs service" style="left:352px;top:279px">
      <svg width="30" height="30" viewBox="0 0 30 30" fill="none" stroke="#f25a1c" stroke-width="1.3"><path d="M5 27V8l10-5 10 5v19z"/><path d="M10 27V12h10v15M10 17h10M10 22h10"/></svg>
      <div><h3>Lift</h3><p>Lorem ipsum dolor sit amet, consectetur adipiscing elit. Ut elit tellus, luctus nec ullamcorper mattis, pulvinar dapibus leo.</p></div>
    </div>
    <div class="abs service" style="left:613px;top:279px">
      <svg width="30" height="30" viewBox="0 0 30 30" fill="none" stroke="#f25a1c" stroke-width="1.3"><path d="M6 26l10-10M14 8l8 8M18 4l8 8-4 4-8-8z"/><path d="M4 10h6M7 7v6"/></svg>
      <div><h3>Fire Safety</h3><p>Lorem ipsum dolor sit amet, consectetur adipiscing elit. Ut elit tellus, luctus nec ullamcorper mattis, pulvinar dapibus leo.</p></div>
    </div>
  </section>

  <section class="process">
    <div class="abs eyebrow" style="top:62px">Get your project done in just 3 steps</div>
    <h2 class="abs sec-title" style="top:82px">Our WorKing Process</h2>
    <div class="abs step" style="left:99px;top:154px"><div class="step-num">01.</div><h3>Architecture Planning</h3><p>Industry is what is sitting on the driving sit of the current world economy. We are here to support that economy.</p></div>
    <div class="abs divider" style="left:345px"></div>
    <div class="abs step" style="left:375px;top:154px"><div class="step-num" style="color:var(--orange)">02.</div><h3>Client Approvement</h3><p>We are complete 1500 project, 100% experience Engineer with manpower 1000%. Construct has established.</p></div>
    <div class="abs divider" style="left:604px"></div>
    <div class="abs step" style="left:634px;top:154px"><div class="step-num">03.</div><h3>Project Completion</h3><p>we have succeeded with so many ups and downs for the past 25 years with the family we built our customers.</p></div>
  </section>

  <section class="projects">
    <div class="abs eyebrow" style="top:60px">Explore our archives</div>
    <h2 class="abs sec-title" style="top:80px">Full Construction Project</h2>
    <div class="abs project" style="left:92px;top:133px"><div class="photo" role="img" aria-label="Building facade with blue sky and orange cladding" style="background:linear-gradient(90deg,#1f74c9 0%,#2d86dc 35%,#e8661e 45%,#4a4f5c 60%,#6b7080 100%)"></div><h3>Metal Roofing</h3><p>Our sense of curiosity brings brands to life, gets them talking, and makes sure they're heard above problem solvers</p><a>Read More</a></div>
    <div class="abs project" style="left:352px;top:133px"><div class="photo" role="img" aria-label="White modern building with orange accents against sky" style="background:linear-gradient(120deg,#8fb6e2 0%,#c9dcf0 40%,#f1f2f4 55%,#e8742c 70%,#7ea5d6 100%)"></div><h3>House Remodelling</h3><p>Our sense of curiosity brings brands to life, gets them talking, and makes sure they're heard above problem solvers</p><a>Read More</a></div>
    <div class="abs project" style="left:613px;top:133px"><div class="photo" role="img" aria-label="Architect drawing plans on a desk" style="background:linear-gradient(135deg,#f3f1ec 0%,#d9d6cf 50%,#f19a4d 80%,#efe9df 100%)"></div><h3>House Refurbishment</h3><p>Our sense of curiosity brings brands to life, gets them talking, and makes sure they're heard above problem solvers</p><a>Read More</a></div>
    <div class="abs project" style="left:92px;top:459px"><div class="photo" role="img" aria-label="Welder in a blue helmet working with sparks" style="background:linear-gradient(135deg,#1c2f55 0%,#3a5480 45%,#d66a2a 70%,#24324f 100%)"></div><h3>Kitchen Remodelling</h3><p>Our sense of curiosity brings brands to life, gets them talking, and makes sure they're heard above problem solvers</p><a>Read More</a></div>
    <div class="abs project" style="left:352px;top:459px"><div class="photo" role="img" aria-label="Worker in safety harness on a blue wall" style="background:linear-gradient(120deg,#2d5ea8 0%,#4c7cc2 40%,#e86a26 60%,#2a4f8c 100%)"></div><h3>Tiling &amp; Florring</h3><p>Our sense of curiosity brings brands to life, gets them talking, and makes sure they're heard above problem solvers</p><a>Read More</a></div>
    <div class="abs project" style="left:613px;top:459px"><div class="photo" role="img" aria-label="Site engineer in orange vest on the phone" style="background:linear-gradient(90deg,#c8c2b8 0%,#a89a88 30%,#f07a2a 55%,#b8ad9c 100%)"></div><h3>Green House Extension</h3><p>Our sense of curiosity brings brands to life, gets them talking, and makes sure they're heard above problem solvers</p><a>Read More</a></div>
  </section>

  <section class="mission">
    <div class="abs mission-panel"></div>
    <h2 class="abs mission-title">Our Mission</h2>
    <p class="abs mission-text">Lorem ipsum, or lipsum as it is sometimes known, is dummy text used in laying out print, graphic or web designs. The passage is attributed to an unknown typesetter in the 15th century who is thought to have scrambled parts of an old Latin treatise on duty and ethics for use in a type specimen book. Easily generate Lorem Ipsum placeholder text in any number of characters, words sentences or paragraphs. earn about the origins of the passage</p>
    <div class="abs btn mission-btn">Get Started</div>
    <div class="photo" role="img" aria-label="Two builders giving a high five on site" style="left:474px;top:0;width:398px;height:321px;background:linear-gradient(120deg,#c9d4e2 0%,#e2c49a 40%,#e6a640 55%,#9fb0c8 100%)"></div>
  </section>

  <section class="team">
    <div class="abs member" style="left:90px;top:45px"><div class="avatar" role="img" aria-label="Team member portrait"><span class="plus">+</span></div><h3>Owen Caldicott</h3><span>Chief Architecture</span></div>
    <div class="abs member" style="left:353px;top:45px"><div class="avatar" role="img" aria-label="Team member portrait"><span class="plus">+</span></div><h3>Tomas Brierley</h3><span>Site Engineer</span></div>
    <div class="abs member" style="left:615px;top:45px"><div class="avatar" role="img" aria-label="Team member portrait"><span class="plus">+</span></div><h3>Dylan Hartwell</h3><span>Site Manager</span></div>
    <div class="abs member" style="left:90px;top:317px"><div class="avatar" role="img" aria-label="Team member portrait"><span class="plus">+</span></div><h3>Marcus Lindell</h3><span>Assistant Engineer</span></div>
    <div class="abs member" style="left:353px;top:317px"><div class="avatar" role="img" aria-label="Team member portrait"><span class="plus">+</span></div><h3>Ravi Okonedo</h3><span>Site Manager</span></div>
    <div class="abs member" style="left:615px;top:317px"><div class="avatar" role="img" aria-label="Team member portrait"><span class="plus">+</span></div><h3>Elliot Farrant</h3><span>Architecture</span></div>
  </section>

  <section class="management" role="img" aria-label="Worker in blue uniform holding a folder in an office">
    <div class="abs mgmt-box">
      <h2>Full Project Management</h2>
      <p>Lorem ipsum dolor sit amet, quam felis adipiscing elit. Aenean commodo ligula eget dolor. Aenean massa. Cum sociis Theme mus.</p>
      <div class="mgmt-btn">Contact Us</div>
    </div>
  </section>

  <section class="testimonials">
    <div class="abs eyebrow" style="top:73px">Testimonials</div>
    <h2 class="abs sec-title" style="top:97px">What Our Clients Say</h2>
    <p class="abs quote">Aenean auctor wisi et urna. Aliquam erat volutpat. Duis ac turpis. Integer rutrum ante eu lacus. Vestibulum libero nisl, porta vel, scelerisque eget, malesuada at, neque. Vivamus eget nibh. Etiam cursus leo vel metus.</p>
    <div class="abs client">Laura Penwick</div>
    <div class="abs client-role">Real Estate Client</div>
    <div class="abs dots"><i></i><i></i><i></i><i></i></div>
  </section>

  <footer class="site-footer">
    <div class="abs f-col" style="left:56px;top:41px"><h4>About Us</h4><p>12 Harbour Row, Eastfield<br>Phone: 55301927<br>Email hello@hwnstructures.co.uk<br>Office Time: 10AM-5PM</p></div>
    <div class="abs f-col" style="left:272px;top:41px"><h4>Quick Links</h4><p>About Us<br>Meet Our Team<br>News &amp; Media<br>Case Studies Grid</p></div>
    <div class="abs f-col" style="left:487px;top:41px"><h4>Opening Time</h4><p>Mon-Tues : 6:00am - 10:00 pm<br>Sunday : 1:00pm - 8:00pm</p><div class="socials"><i></i><i></i><i></i></div></div>
    <div class="abs f-col" style="left:703px;top:41px"><h4>Recent Project</h4><div class="thumbs" role="img" aria-label="Thumbnails of recently completed interiors"><div></div><div></div><div></div><div></div><div></div><div></div></div></div>
    <div class="abs f-bottom">All Right Reserved . HWN Structures Ltd</div>
  </footer>

</div>
</body>
</html>
```